Business Card Design Project

I have a newly designed logo (by Marlo through Pixel Harbor) and now need a business card concept / design.

We are an HR consulting firm.

I am hoping that someone can advise me if they are able to see the logo that I chose in my last project (logo design) or if I need to upload that logo here in this project?

Obviously I want the business card to fit with the logo!

Industry/Entity Type

Business

```html
<!DOCTYPE html>
<html lang="en">
<head>
<meta charset="utf-8">
<title>Harwell Consulting — Business Card</title>
<link href="https://fonts.googleapis.com/css2?family=Questrial&display=swap" rel="stylesheet">
<style>
  :root {
    --page-bg: #d9dadb;
    --card-white: #ffffff;
    --card-dark-top: #1c1c1c;
    --card-dark-bottom: #000000;
    --ink-dark: #3a3f44;
    --accent: #1b8fc4;
    --marker: #b9bec2;
    --text-light: #f2f2f2;
    --text-muted: #b0b0b0;
  }
  * { box-sizing: border-box; margin: 0; padding: 0; }
  html, body { width: 857px; height: 1200px; overflow: hidden; }
  body {
    background: var(--page-bg);
    font-family: "Questrial", "Century Gothic", sans-serif;
    display: flex;
    flex-direction: column;
    align-items: center;
    justify-content: center;
    gap: 110px;
  }
  .card {
    width: 700px;
    height: 400px;
    border-radius: 28px;
    position: relative;
    overflow: hidden;
    box-shadow: 0 8px 24px rgba(0,0,0,0.25);
  }

  /* Front */
  .card-front {
    background: var(--card-white);
    display: flex;
    align-items: center;
    justify-content: center;
  }
  .company {
    display: flex;
    align-items: center;
    gap: 20px;
  }
  .company-marker {
    width: 40px;
    height: 40px;
    border-radius: 50%;
    background: var(--marker);
    flex-shrink: 0;
  }
  .company-name {
    font-size: 46px;
    color: var(--ink-dark);
    line-height: 1;
  }

  /* Back */
  .card-back {
    background: linear-gradient(160deg, var(--card-dark-top) 0%, var(--card-dark-bottom) 70%);
  }
  .back-company {
    position: absolute;
    top: 40px;
    left: 36px;
  }
  .back-company .company-marker { width: 24px; height: 24px; background: #5c6166; }
  .back-company .company-name { font-size: 26px; color: var(--text-light); }

  .contact {
    position: absolute;
    right: 40px;
    top: 150px;
    text-align: right;
    color: var(--text-light);
    line-height: 1.25;
  }
  .contact-name { font-size: 24px; }
  .contact-role { font-size: 20px; color: var(--text-muted); margin-bottom: 30px; }
  .contact-value { font-size: 21px; color: var(--accent); }
  .contact-label { font-size: 17px; color: var(--text-light); margin-bottom: 16px; }
</style>
</head>
<body>

  <section class="card card-front" aria-label="Card front">
    <div class="company">
      <span class="company-marker" aria-hidden="true"></span>
      <div class="company-name">Harwell Consulting</div>
    </div>
  </section>

  <section class="card card-back" aria-label="Card back">
    <div class="company back-company">
      <span class="company-marker" aria-hidden="true"></span>
      <div class="company-name">Harwell Consulting</div>
    </div>

    <div class="contact">
      <div class="contact-name">Tessa Harwell</div>
      <div class="contact-role">Director</div>
      <div class="contact-value">www.harwellconsulting.com</div>
      <div class="contact-label">website</div>
      <div class="contact-value">tessa@harwellconsulting.com</div>
      <div class="contact-label">e-mail</div>
    </div>
  </section>

</body>
</html>
```